Fern and Bough Tree Services Business Card Design

We need a business card design for our company based in Melbourne, Australia. We are a tree services business. We already have a logo designed by a designer on graphic hive, so obviously we would like this to be incorporated in to the design, including similar colours. The final design should be sleek.

It should have:

Marcus Whitfield
Chief Executive Officer

www.fernandbough.com.au
marcus.whitfield@fernandbough.com.au
0417 293 865

Industry/Entity Type

Business

```html
<!DOCTYPE html>
<html lang="en">
<head>
<meta charset="utf-8">
<title>Fern and Bough Tree Services – Business Card</title>
<link rel="stylesheet" href="https://fonts.googleapis.com/css2?family=Tinos:wght@400;700&display=swap">
<style>
  :root {
    --backdrop: #d9d9d9;
    --card: #ebecec;
    --ink: #1e1e1e;
    --ink-soft: #2c2c2c;
    --leaf-green: #7dd12b;
    --rule: #555555;
  }
  * { margin: 0; padding: 0; box-sizing: border-box; }
  html, body {
    width: 1200px;
    height: 900px;
    overflow: hidden;
    background: var(--backdrop);
  }
  .canvas {
    width: 1200px;
    height: 900px;
    display: flex;
    align-items: center;
    justify-content: center;
  }
  .business-card {
    position: relative;
    width: 480px;
    height: 800px;
    background: var(--card);
    border-radius: 4px;
    box-shadow: 0 6px 24px rgba(0, 0, 0, 0.18);
    font-family: "Tinos", "Times New Roman", serif;
    color: var(--ink);
    text-align: center;
    overflow: hidden;
  }
  .brand-mark {
    display: block;
    width: 150px;
    height: 150px;
    margin: 70px auto 0;
    border-radius: 50%;
    background: var(--leaf-green);
  }
  .brand-name {
    margin-top: 34px;
    font-size: 36px;
    font-weight: 400;
    line-height: 1.1;
    color: var(--ink);
  }
  .person {
    margin-top: 130px;
  }
  .person-name {
    font-size: 36px;
    font-weight: 700;
    color: var(--ink);
  }
  .person-title {
    margin-top: 4px;
    font-size: 22px;
    color: var(--ink-soft);
  }
  .dotted-rule {
    width: 400px;
    margin: 10px auto;
    border: 0;
    border-top: 1.5px dotted var(--rule);
  }
  .contact {
    list-style: none;
    margin-top: 16px;
  }
  .contact li { line-height: 1.35; }
  .contact .email { font-size: 19px; }
  .contact .phone { font-size: 22px; }
  .contact .website { font-size: 29px; margin-top: 2px; }
  .footer-band {
    position: absolute;
    left: 0;
    right: 0;
    bottom: 0;
    height: 96px;
  }
  .footer-band .black-line {
    height: 6px;
    background: var(--ink);
  }
  .footer-band .green-band {
    height: 84px;
    margin-top: 6px;
    background: var(--leaf-green);
  }
</style>
</head>
<body>
<main class="canvas">
  <article class="business-card">
    <span class="brand-mark" aria-hidden="true"></span>
    <h1 class="brand-name">Fern and Bough<br>Tree Services</h1>

    <section class="person">
      <h2 class="person-name">Marcus Whitfield</h2>
      <p class="person-title">Chief Executive Officer</p>
    </section>

    <hr class="dotted-rule">

    <hr class="dotted-rule">

    <ul class="contact">
      <li class="email">marcus.whitfield@fernandbough.com.au</li>
      <li class="phone">Phone: (0417)-293-865</li>
      <li class="website">www.fernandbough.com.au</li>
    </ul>

    <div class="footer-band" aria-hidden="true">
      <div class="black-line"></div>
      <div class="green-band"></div>
    </div>
  </article>
</main>
</body>
</html>
```